dessert restaurant

I need a business card design for my restaurant. It will primarily be a dessert and wine restaurant. I will serve delicious baked from scratch desserts, cake, pies cookies brownies etc. Select red and white wines.I will also offer light breakfast, and lunch menu. This will be an upscale contemporary design restaurant with reasonably priced items on the menu. I will also offer small plates in the evening with dessert menu. my color scheme is cobalt blue , red, white black. My restaurant will be the place where adults come after enjoying the meal at a restaurant and want to enjoy a dessert and a glass of wine to finish off their evening. I will also have contemporary jazz sounds for atmosphere.

Industry/Entity Type

Restaurant

Contact Information for Business Card

delia marsh 415 862 3094

```html
<!DOCTYPE html>
<html lang="en">
<head>
<meta charset="utf-8">
<title>Velour – Business Card</title>
<link href="https://fonts.googleapis.com/css2?family=Arimo:wght@400;700&display=swap" rel="stylesheet">
<style>
  :root {
    --page-bg: #e9e4df;
    --card-white: #ffffff;
    --band-dark: #4f2517;
    --band-light: #6e4b3f;
    --ink: #5b3a2e;
    --ink-soft: #6d5047;
  }
  * { margin: 0; padding: 0; box-sizing: border-box; }
  html, body {
    width: 1200px; height: 800px; overflow: hidden;
    background: var(--page-bg);
    font-family: "Arimo", Arial, sans-serif;
    color: var(--ink);
  }
  .card {
    position: absolute; left: 100px; top: 114px;
    width: 1000px; height: 572px;
    background: var(--card-white);
    box-shadow: 0 12px 30px rgba(60, 35, 25, 0.25);
    overflow: hidden;
  }
  .band {
    position: absolute; left: 0; width: 100%; height: 72px;
    background: linear-gradient(90deg, var(--band-dark), var(--band-light));
  }
  .band--top { top: 0; }
  .band--bottom { bottom: 0; }
  .rule {
    position: absolute; left: 0; width: 100%; height: 2px;
    background: var(--ink);
  }
  .rule--top { top: 84px; }
  .rule--bottom { bottom: 84px; }
  .brand {
    position: absolute; left: 40px; top: 200px;
    width: 500px; height: 172px;
    display: flex; align-items: center; justify-content: center;
  }
  .brand__name {
    font-size: 64px; font-weight: 700; letter-spacing: 6px;
    color: var(--ink);
  }
  .divider {
    position: absolute; left: 590px; top: 175px;
    width: 2px; height: 240px; background: var(--ink);
  }
  .contact {
    position: absolute; left: 630px; top: 190px; width: 340px;
  }
  .contact__name {
    font-size: 36px; font-weight: 700; letter-spacing: 1px;
    color: var(--ink-soft); word-spacing: 10px;
  }
  .contact__title {
    font-size: 22px; color: var(--ink-soft);
    margin-top: 2px; word-spacing: 8px;
  }
  .contact__list { list-style: none; margin-top: 34px; }
  .contact__item {
    display: flex; align-items: flex-start; gap: 12px;
    font-size: 20px; line-height: 28px; color: var(--ink-soft);
    word-spacing: 6px;
  }
  .contact__icon { width: 16px; height: 16px; margin-top: 6px; flex: none; fill: var(--ink); }
</style>
</head>
<body>
  <div class="card">
    <div class="band band--top"></div>
    <div class="rule rule--top"></div>

    <div class="brand">
      <span class="brand__name">VELOUR</span>
    </div>

    <div class="divider"></div>

    <div class="contact">
      <p class="contact__name">Delia Marsh</p>
      <p class="contact__title">Managing Director</p>
      <ul class="contact__list">
        <li class="contact__item">
          <svg class="contact__icon" viewBox="0 0 16 16"><path d="M3.5 1l2.5 3-1.5 2a9 9 0 0 0 5.5 5.5l2-1.5 3 2.5-1.5 2.5C7 15 1 9 1 2.5z"/></svg>
          <span>415 862 3094</span>
        </li>
        <li class="contact__item">
          <svg class="contact__icon" viewBox="0 0 16 16"><circle cx="8" cy="8" r="7" fill="none" stroke="currentColor" stroke-width="1.6" style="stroke:var(--ink)"/><path d="M1 8h14M8 1c-3 3.5-3 10.5 0 14M8 1c3 3.5 3 10.5 0 14" fill="none" style="stroke:var(--ink)" stroke-width="1.2"/></svg>
          <span>www.yourwebsite.com</span>
        </li>
        <li class="contact__item">
          <svg class="contact__icon" viewBox="0 0 16 16"><path d="M8 0a5.5 5.5 0 0 0-5.5 5.5C2.5 10 8 16 8 16s5.5-6 5.5-10.5A5.5 5.5 0 0 0 8 0zm0 8a2.5 2.5 0 1 1 0-5 2.5 2.5 0 0 1 0 5z"/></svg>
          <span>2417 Harmon Ave<br>N.E. Portland OR 97212</span>
        </li>
      </ul>
    </div>

    <div class="rule rule--bottom"></div>
    <div class="band band--bottom"></div>
  </div>
</body>
</html>
```